Professional Home Buyer business card needed

I need a pretty straight forward business card designed. We help people that NEED to sell their homes solve problems. We perform all types of Real Estate transactions including flip, wholesale, investment, rental property and multi family. The card will mainly be used to give to prospective Sellers but will also be given to Real Estate Investors as well. It should professional and very easy to read, most clients are older people.

Target Market(s)

Distressed home sellers as well as Real Estate investors

Industry/Entity Type

Real Estate

Contact Information for Business Card

should be a professional layout

Colors
ec1f27
ffffff
000000

Requirements
Must have
• Large logo on back and smaller one on front. should utilize Red, white, and black.
• I am thinking of using a soft touch coating on the card so keep that in mind.
• Contact info should be very easy to read, think older clients.
Nice to have
• I would like to see a design with rounded corners on the card
Should not have
• pictures of homes or other home graphics.

```html
<!DOCTYPE html>
<html lang="en">
<head>
<meta charset="utf-8">
<title>Keystone Home Buyers – Business Card</title>
<link href="https://fonts.googleapis.com/css2?family=Open+Sans:wght@400;600;700;800&display=swap" rel="stylesheet">
<style>
  :root {
    --brand-red: #ec1f27;
    --brand-black: #000000;
    --ink: #1e1e1e;
    --card-white: #ffffff;
    --backdrop: #5e5e5e;
    --rule-grey: #7a7a7a;
    --band-dark: #231f20;
  }
  * { margin: 0; padding: 0; box-sizing: border-box; }
  html, body {
    width: 1200px; height: 1200px; overflow: hidden;
    background: var(--backdrop);
    font-family: "Open Sans", Arial, sans-serif;
  }
  .card {
    position: absolute;
    left: 240px; width: 720px; height: 418px;
    background: var(--card-white);
    border-radius: 34px;
    overflow: hidden;
  }
  .card--front { top: 142px; }
  .card--back { top: 640px; }

  /* Brand lockup */
  .brand {
    position: absolute;
    display: flex; flex-direction: column; align-items: center;
  }
  .brand__tagline {
    font-weight: 700; letter-spacing: 0.3em; color: var(--ink);
    text-transform: uppercase; white-space: nowrap;
  }
  .brand__row { display: flex; align-items: center; }
  .brand__mark { background: var(--brand-red); flex: none; }
  .brand__name {
    font-weight: 800; color: var(--brand-black);
    text-transform: uppercase; white-space: nowrap; line-height: 1.05;
  }
  .brand__name span { display: block; }

  .card--front .brand { left: 0; right: 0; top: 122px; }
  .card--front .brand__tagline { font-size: 15px; margin-bottom: 16px; }
  .card--front .brand__row { gap: 18px; }
  .card--front .brand__mark { width: 30px; height: 30px; }
  .card--front .brand__name { font-size: 40px; }

  .card--back .brand { left: 74px; top: 78px; align-items: flex-start; }
  .card--back .brand__tagline { font-size: 9px; margin-bottom: 8px; }
  .card--back .brand__row { gap: 10px; }
  .card--back .brand__mark { width: 18px; height: 18px; }
  .card--back .brand__name { font-size: 22px; }

  /* Person */
  .person {
    position: absolute; right: 78px; top: 218px; text-align: right;
  }
  .person__name { font-size: 25px; font-weight: 700; color: var(--brand-red); line-height: 1.2; }
  .person__title { font-size: 16px; font-weight: 600; color: var(--ink); margin-top: 4px; }

  .divider { position: absolute; left: 74px; right: 78px; top: 282px; height: 4px; }
  .divider__grey { position: absolute; left: 0; right: 0; top: 1px; height: 1.5px; background: var(--rule-grey); }
  .divider__red { position: absolute; right: 0; width: 180px; top: 0; height: 3.5px; background: var(--brand-red); }

  .contact {
    position: absolute; list-style: none;
    font-size: 16px; font-weight: 400; color: var(--ink);
  }
  .contact li { display: flex; align-items: center; gap: 10px; height: 24px; }
  .contact svg { width: 15px; height: 15px; fill: var(--brand-red); flex: none; }
  .contact--phone { left: 74px; top: 301px; }
  .contact--online { left: 364px; top: 300px; }

  .band { position: absolute; left: 0; bottom: 0; width: 720px; height: 32px; }
</style>
</head>
<body>

<section class="card card--front" aria-label="Card front">
  <div class="brand">
    <p class="brand__tagline">Solutions for sellers!</p>
    <div class="brand__row">
      <span class="brand__mark"></span>
      <p class="brand__name"><span>Keystone</span><span>Home Buyers</span></p>
    </div>
  </div>
</section>

<section class="card card--back" aria-label="Card back">
  <div class="brand">
    <p class="brand__tagline">Solutions for sellers!</p>
    <div class="brand__row">
      <span class="brand__mark"></span>
      <p class="brand__name"><span>Keystone</span><span>Home Buyers</span></p>
    </div>
  </div>

  <div class="person">
    <p class="person__name">Dale Hartwell</p>
    <p class="person__title">President</p>
  </div>

  <div class="divider">
    <span class="divider__grey"></span>
    <span class="divider__red"></span>
  </div>

  <ul class="contact contact--phone">
    <li>
      <svg viewBox="0 0 24 24" aria-hidden="true"><path d="M6.6 10.8a15.1 15.1 0 0 0 6.6 6.6l2.2-2.2c.3-.3.7-.4 1-.2 1.1.4 2.3.6 3.6.6.6 0 1 .4 1 1V20c0 .6-.4 1-1 1A17 17 0 0 1 3 4c0-.6.4-1 1-1h3.5c.6 0 1 .4 1 1 0 1.3.2 2.5.6 3.6.1.3 0 .7-.2 1z"/></svg>
      <span>316-555-0148</span>
    </li>
  </ul>

  <ul class="contact contact--online">
    <li>
      <svg viewBox="0 0 24 24" aria-hidden="true"><rect x="2" y="5" width="20" height="14" rx="1.5"/><polyline points="3,6.5 12,13 21,6.5" fill="none" stroke="#fff" stroke-width="2"/></svg>
      <span>dale@prairiehomesforcash.com</span>
    </li>
    <li>
      <svg viewBox="0 0 24 24" aria-hidden="true"><path d="M12 2a10 10 0 1 0 0 20 10 10 0 0 0 0-20zm6.9 6h-3a15 15 0 0 0-1.3-3.9A8 8 0 0 1 18.9 8zM12 4c.8 1.2 1.5 2.5 1.9 4h-3.8c.4-1.5 1.1-2.8 1.9-4zM4.3 14a8 8 0 0 1 0-4h3.4a16 16 0 0 0 0 4zm.8 2h3a15 15 0 0 0 1.3 3.9A8 8 0 0 1 5.1 16zm3-8h-3a8 8 0 0 1 4.3-3.9C8.8 5.3 8.4 6.6 8.1 8zM12 20c-.8-1.2-1.5-2.5-1.9-4h3.8c-.4 1.5-1.1 2.8-1.9 4zm2.3-6H9.7a14 14 0 0 1 0-4h4.6a14 14 0 0 1 0 4zm.3 5.9c.6-1.2 1-2.5 1.3-3.9h3a8 8 0 0 1-4.3 3.9zm1.7-5.9a16 16 0 0 0 0-4h3.4a8 8 0 0 1 0 4z"/></svg>
      <span>www.prairiehomesforcash.com</span>
    </li>
  </ul>

  <svg class="band" viewBox="0 0 720 32" preserveAspectRatio="none" aria-hidden="true">
    <polygon points="0,0 540,0 532,32 0,32" fill="var(--brand-red)"/>
    <polygon points="554,0 720,0 720,32 546,32" fill="var(--band-dark)"/>
  </svg>
</section>

</body>
</html>
```